Cover für ein Taschenbuch zum Thema Ruhestand gesucht!
Zielgruppe
Unsere Zielgruppe sind Senioren, bzw. Menschen im Alter 50+. Es handelt sich bei dem Buch um einen Ratgeber zum Thema 'Ruhestand'. Allerdings wird das Buch ebenso von einer jüngeren Zielgruppe gekauft, da der Ratgeber auch gerne an Eltern oder Großeltern verschenkt wird.
Aufgabenstellung
siehe Dateiupload
Format: 5,25' x 8'

```html
<!DOCTYPE html>
<html lang="de">
<head>
<meta charset="utf-8">
<title>IHR Ruhestand – Buchcover</title>
<link href="https://fonts.googleapis.com/css2?family=Arimo:ital,wght@0,400;1,400&family=Yanone+Kaffeesatz:wght@300;400&display=swap" rel="stylesheet">
<style>
  :root {
    --teal-dark: #2a6470;
    --teal-shadow: #6c9ea6;
    --title-light: #c9ebf0;
    --sky-top: #8fd0d7;
    --sky-bottom: #cde9eb;
    --wave-light: rgba(255,255,255,0.35);
    --sand: #fbfbfa;
    --ink: #0b0b0b;
  }
  * { margin: 0; padding: 0; box-sizing: border-box; }
  html, body { width: 788px; height: 1200px; overflow: hidden; background: var(--sand); }
  .cover {
    position: relative;
    width: 788px;
    height: 1200px;
    overflow: hidden;
    background: linear-gradient(180deg, var(--sky-top) 0%, var(--sky-bottom) 65%, #d8eeee 100%);
  }
  .cover__shapes { position: absolute; inset: 0; }
  .cover__title {
    position: absolute;
    left: 46px;
    top: 40px;
    font-family: "Arimo", Arial, sans-serif;
    font-weight: 400;
    font-size: 106px;
    line-height: 1;
    letter-spacing: 1px;
    color: var(--title-light);
    white-space: nowrap;
  }
  .cover__tagline {
    position: absolute;
    left: 40px;
    top: 222px;
    font-family: "Yanone Kaffeesatz", "Arial Narrow", sans-serif;
    font-weight: 300;
    font-size: 76px;
    line-height: 64px;
    color: var(--teal-dark);
    transform: rotate(11deg);
    transform-origin: left top;
    white-space: nowrap;
  }
  .cover__tagline span { display: block; }
  .cover__tagline .line-two { padding-left: 96px; }
  .cover__lead {
    position: absolute;
    left: 38px;
    top: 560px;
    font-family: "Arimo", Arial, sans-serif;
    font-style: italic;
    font-size: 33px;
    line-height: 51px;
    color: var(--ink);
  }
  .cover__photo {
    position: absolute;
    left: 0;
    top: 815px;
    width: 788px;
    height: 290px;
  }
  .cover__author {
    position: absolute;
    left: 116px;
    top: 1128px;
    font-family: "Yanone Kaffeesatz", "Arial Narrow", sans-serif;
    font-weight: 300;
    font-size: 56px;
    line-height: 1;
    letter-spacing: 29px;
    color: var(--teal-dark);
    white-space: nowrap;
  }
</style>
</head>
<body>
<main class="cover">
  <svg class="cover__shapes" width="788" height="1200" viewBox="0 0 788 1200" aria-hidden="true">
    <!-- soft light waves -->
    <path d="M0 420 C120 470 300 440 470 330 C600 250 760 300 745 420 C735 520 680 560 560 600 C400 650 200 540 0 520 Z" fill="var(--wave-light)"/>
    <path d="M0 450 C150 520 350 540 560 530 C700 525 740 560 720 640 C690 720 500 760 300 770 C180 775 80 770 0 760 Z" fill="var(--wave-light)"/>
    <path d="M0 600 C200 620 450 640 640 700 C560 760 300 800 0 830 Z" fill="rgba(255,255,255,0.18)"/>
    <!-- shadow band under header -->
    <path d="M0 140 C200 230 480 250 788 142 L788 185 C500 265 200 250 0 175 Z" fill="var(--teal-shadow)" opacity="0.75"/>
    <path d="M0 136 C200 224 480 244 788 138" fill="none" stroke="#ffffff" stroke-width="1.5" opacity="0.9"/>
    <!-- dark header band -->
    <path d="M0 0 H788 V140 C500 240 220 225 0 128 Z" fill="var(--teal-dark)"/>
  </svg>

  <h1 class="cover__title">IHR Ruhestand</h1>

  <p class="cover__tagline">
    <span class="line-one">Das Beste kommt</span>
    <span class="line-two">immer zum Schluss !</span>
  </p>

  <p class="cover__lead">Die besten Strategien und Tipps,<br>mit denen Sie Ihre Rentenzeit in<br>vollen Zügen genießen können</p>

  <svg class="cover__photo" width="788" height="290" viewBox="0 0 788 290" role="img" aria-label="Foto: zwei hölzerne Sonnenliegen mit grünen Auflagen und ein kleiner Tisch am weißen Sandstrand vor türkisem Meer">
    <defs>
      <linearGradient id="beachFill" x1="0" y1="0" x2="0" y2="1">
        <stop offset="0" stop-color="#cfe9ea" stop-opacity="0"/>
        <stop offset="0.55" stop-color="#c9a07a" stop-opacity="0.55"/>
        <stop offset="0.78" stop-color="#4fb3b0"/>
        <stop offset="0.92" stop-color="#7cc8c2"/>
        <stop offset="1" stop-color="#fbfbfa"/>
      </linearGradient>
    </defs>
    <rect width="788" height="290" fill="url(#beachFill)"/>
  </svg>

  <p class="cover__author">Matthias Brenner</p>
</main>
</body>
</html>
```